Flyer Template

I need a flyer template for door knocking on properties. Text Boxes need to be editable, with a header and text body. Footer to be my info. Project to be stylized to match my real estate signs and logo art from past projects

```html
<!DOCTYPE html>
<html lang="en">
<head>
<meta charset="UTF-8">
<title>Brantley Realty – Just Listed Flyer</title>
<link href="https://fonts.googleapis.com/css2?family=Josefin+Sans:wght@600;700&family=Montserrat:wght@700;800&family=Open+Sans:wght@400;600&display=swap" rel="stylesheet">
<style>
  :root {
    --red: #d81f26;
    --black: #0d0d0d;
    --charcoal: #1e1e20;
    --white: #ffffff;
    --ink: #161616;
    --body-gray: #5a5a5a;
    --backdrop: #e9e9e7;
  }
  * { box-sizing: border-box; margin: 0; padding: 0; }
  html, body {
    width: 1200px; height: 767px; overflow: hidden;
    background: var(--backdrop);
  }
  .canvas { position: relative; width: 1200px; height: 767px; }
  .flyer {
    position: absolute; left: 314px; top: 13px;
    width: 612px; height: 792px;
    transform: scale(0.934); transform-origin: top left;
    background: var(--white); overflow: hidden;
    box-shadow: 0 6px 22px rgba(0,0,0,.25);
    font-family: "Open Sans", sans-serif;
  }
  .hero-photo {
    position: absolute; left: 0; top: 0; width: 612px; height: 300px;
    background: linear-gradient(180deg, #e7eef3 0%, #cfc6bb 35%, #8f7a6a 62%, #5d7a3f 82%, #4f7a2c 100%);
  }
  .hero-rule { position: absolute; left: 0; top: 300px; width: 612px; height: 5px; background: #b9b9b9; }
  .ribbon {
    position: absolute; right: -52px; top: 38px; width: 220px; height: 28px;
    background: var(--red); color: var(--white);
    transform: rotate(45deg);
    font-family: "Montserrat", sans-serif; font-weight: 700; font-size: 13px;
    letter-spacing: 1px; text-align: center; line-height: 28px;
  }
  .brand { position: absolute; left: 29px; top: 320px; width: 260px; }
  .brand-mark { width: 22px; height: 22px; background: var(--red); margin: 40px 0 18px 114px; }
  .brand-name {
    font-family: "Josefin Sans", sans-serif; font-weight: 700;
    font-size: 26px; color: var(--ink); letter-spacing: .3px; line-height: 1;
  }
  .intro {
    position: absolute; left: 29px; top: 448px; width: 258px;
    font-size: 12px; line-height: 16px; color: var(--body-gray); text-align: justify;
  }
  .intro p + p { margin-top: 16px; }
  .gallery .photo { position: absolute; border: 2px solid var(--white); }
  .photo.kitchen { left: 322px; top: 317px; width: 122px; height: 121px; background: linear-gradient(160deg, #f1f1ef, #cfcac4 60%, #6b5443); }
  .photo.living { left: 447px; top: 317px; width: 156px; height: 248px; background: linear-gradient(170deg, #eeeeeb, #cdc9c4 55%, #8c8580); }
  .photo.nook { left: 322px; top: 442px; width: 122px; height: 123px; background: linear-gradient(170deg, #b7aa9b, #e5e2de 50%, #a39b93); }
  .red-band { position: absolute; left: 0; top: 0; width: 612px; height: 792px; }
  .pitch { position: absolute; left: 29px; top: 581px; width: 258px; color: var(--white); }
  .pitch h2 {
    font-family: "Montserrat", sans-serif; font-weight: 800; font-size: 12.5px;
    letter-spacing: .3px; margin-bottom: 16px;
  }
  .pitch p { font-size: 12.2px; line-height: 16px; text-align: justify; }
  .features { position: absolute; left: 330px; top: 597px; width: 280px; }
  .feature { position: absolute; display: flex; align-items: center; width: 140px; color: var(--white); }
  .feature-icon {
    width: 46px; height: 46px; border: 2px solid var(--white); border-radius: 50%;
    display: flex; align-items: center; justify-content: center; flex: none;
  }
  .feature-text { margin-left: 12px; font-size: 10px; line-height: 16px; }
  .footer-phone {
    position: absolute; left: 40px; top: 757px; display: flex; align-items: center;
    color: var(--white); font-family: "Montserrat", sans-serif; font-weight: 700; font-size: 23px; letter-spacing: .5px;
  }
  .footer-phone svg { margin-right: 20px; }
  .footer-email {
    position: absolute; left: 352px; top: 770px; display: flex; align-items: center;
    color: var(--white); font-family: "Montserrat", sans-serif; font-weight: 700; font-size: 14px; letter-spacing: 1px;
  }
  .footer-email svg { margin-right: 9px; }
</style>
</head>
<body>
<div class="canvas">
  <article class="flyer">
    <div class="hero-photo" role="img" aria-label="Photo of a two-storey brick family home with a green lawn"></div>
    <div class="hero-rule"></div>
    <div class="ribbon">JUST LISTED</div>

    <svg class="red-band" viewBox="0 0 612 792" aria-hidden="true">
      <polygon points="0,557 300,557 316,584 612,584 612,756 316,756 316,745 0,745" fill="var(--red)"/>
      <polygon points="0,745 306,745 336,792 0,792" fill="var(--black)"/>
      <polygon points="316,764 612,764 612,792 334,792" fill="var(--charcoal)"/>
    </svg>

    <header class="brand">
      <div class="brand-mark"></div>
      <h1 class="brand-name">BRANTLEY REALTY</h1>
    </header>

    <div class="intro">
      <p>Ut wisi enim ad minim veniam, quis nostrud exerci tation ullamcorper suscipit lobortis nisl ut aliquip ex ea commodo consequat.</p>
      <p>Duis autem vel eum iriure dolor in hendrerit in vulputate velit esse molestie consequat,</p>
    </div>

    <div class="gallery">
      <div class="photo kitchen" role="img" aria-label="Photo of a white kitchen with bar stools"></div>
      <div class="photo living" role="img" aria-label="Photo of a bright living room with grey sofa and rug"></div>
      <div class="photo nook" role="img" aria-label="Photo of a reading nook with armchair"></div>
    </div>

    <section class="pitch">
      <h2>LOREM IPSUM DOLOR SIT AMET</h2>
      <p>consectetuer adipiscing elit, sed diam nonummy nibh euismod tincidunt ut laoreet dolore magna aliquam erat volutpat. Ut wisi enim ad minim veniam, quis nostrud exerci tation ullamcorper suscipit lobortis nisl ut aliquip ex ea commodo consequat. Duis autem vel eum iriure dolor in</p>
    </section>

    <section class="features">
      <div class="feature" style="left:0;top:0">
        <div class="feature-icon"><svg width="24" height="24" viewBox="0 0 24 24" fill="none" stroke="#fff" stroke-width="2"><rect x="3" y="5" width="16" height="16"/><path d="M3 13h7v8M12 5v5"/></svg></div>
        <div class="feature-text">Living Area<br>250m²</div>
      </div>
      <div class="feature" style="left:152px;top:0">
        <div class="feature-icon"><svg width="24" height="24" viewBox="0 0 24 24" fill="none" stroke="#fff" stroke-width="2"><path d="M3 12l9-8 9 8M6 10v10h12V10"/><circle cx="12" cy="15" r="2"/></svg></div>
        <div class="feature-text">Utlities<br>Included</div>
      </div>
      <div class="feature" style="left:0;top:50px">
        <div class="feature-icon"><svg width="26" height="24" viewBox="0 0 26 24" fill="#fff"><rect x="2" y="12" width="22" height="5"/><rect x="4" y="7" width="18" height="5" rx="2"/><rect x="2" y="17" width="2" height="3"/><rect x="22" y="17" width="2" height="3"/></svg></div>
        <div class="feature-text">Bedroom<br>3</div>
      </div>
      <div class="feature" style="left:152px;top:50px">
        <div class="feature-icon"><svg width="26" height="24" viewBox="0 0 26 24" fill="none" stroke="#fff" stroke-width="2"><path d="M2 12h22c0 5-4 7-11 7S2 17 2 12zM18 12V5l3 2"/></svg></div>
        <div class="feature-text">Bathroom<br>2.5</div>
      </div>
      <div class="feature" style="left:0;top:104px">
        <div class="feature-icon"><svg width="26" height="22" viewBox="0 0 26 22" fill="#fff"><path d="M3 11l3-6h14l3 6v6H3z"/><rect x="4" y="17" width="4" height="3"/><rect x="18" y="17" width="4" height="3"/></svg></div>
        <div class="feature-text">Car Garage<br>2</div>
      </div>
      <div class="feature" style="left:152px;top:104px">
        <div class="feature-icon"><svg width="24" height="24" viewBox="0 0 24 24" fill="none" stroke="#fff" stroke-width="2"><path d="M4 20l8-8M5 9a10 10 0 0 0 10 10M13 4a7 7 0 0 1 7 7M13 8a3 3 0 0 1 3 3"/></svg></div>
        <div class="feature-text">Cable TV<br>and WIFI</div>
      </div>
    </section>

    <div class="footer-phone">
      <svg width="24" height="24" viewBox="0 0 24 24" fill="var(--red)"><path d="M6 2l4 5-2 3c1 3 3 5 6 6l3-2 5 4-3 4C10 21 3 14 2 5z"/></svg>
      <span>907-555-0148</span>
    </div>
    <div class="footer-email">
      <svg width="18" height="13" viewBox="0 0 18 13"><rect width="18" height="13" fill="var(--red)"/><path d="M0 0l9 7 9-7" fill="none" stroke="#fff" stroke-width="1.5"/></svg>
      <span>MBRANTLEY@MAILBOX.COM</span>
    </div>
  </article>
</div>
</body>
</html>
```